PuraVeln

Hi, We are looking for a design Label for our Packaged Drinking Water. We want a label in rich color. The current Label is uploaded. We wish for a much brighter color rather than black. Our current label is in black. We have attached other company labels to give you idea. The Solmira bottle image is also uploaded they use sticker for their bottle, front sticker contains name and back sticker's inner portion has graphics and the outer side has information we also open to that.
Industry/Entity Type
Packaged Drinking Water Bottle Brand
Look and feel
Each slider illustrates characteristics of the customer's brand and the style your logo design should communicate.

```html
<!DOCTYPE html>
<html lang="en">
<head>
<meta charset="utf-8">
<title>PuraVeln Packaged Drinking Water – Wrap Label</title>
<link rel="stylesheet" href="https://fonts.googleapis.com/css2?family=Barlow+Condensed:wght@400;500;600&display=swap">
<style>
  :root {
    --page-bg: #e8eff3;
    --label-light: #45a6da;
    --label-mid: #3993d2;
    --label-deep: #2d86cb;
    --tab-dark: #2a7cc0;
    --ink: #ffffff;
    --ink-soft: rgba(255,255,255,0.92);
    --art-hi: rgba(255,255,255,0.55);
    --art-lo: rgba(255,255,255,0.12);
  }
  * { margin: 0; padding: 0; box-sizing: border-box; }
  html, body { width: 1000px; height: 1200px; overflow: hidden; }
  body {
    background: var(--page-bg);
    font-family: "Barlow Condensed", "Arial Narrow", sans-serif;
    color: var(--ink);
    position: relative;
  }
  .wrap-label {
    position: absolute;
    left: 30px; top: 460px;
    width: 940px; height: 281px;
    background: linear-gradient(90deg, var(--label-light) 0%, var(--label-mid) 45%, var(--label-deep) 100%);
  }
  .edge-tab {
    position: absolute; right: 0; width: 23px; height: 39px;
    background: var(--tab-dark);
  }
  .edge-tab--top { top: 0; }
  .edge-tab--bottom { bottom: 0; }

  .block { position: absolute; line-height: 1.35; white-space: nowrap; }
  .caption { font-size: 9px; font-weight: 400; }
  .name { font-size: 11.5px; font-weight: 500; }
  .address { font-size: 8.6px; font-weight: 400; line-height: 1.45; }

  /* Left panel */
  .maker { left: 37px; top: 25px; }
  .marketer { left: 37px; top: 80px; }
  .maker .name, .marketer .name { margin: 2px 0 3px; }

  .cert-badge { position: absolute; background: var(--ink-soft); }
  .cert-badge--food { left: 60px; top: 147px; width: 76px; height: 28px; border-radius: 4px; }
  .cert-badge--std { left: 193px; top: 152px; width: 34px; height: 30px; border-radius: 3px; }
  .std-code { left: 194px; top: 138px; font-size: 8px; }
  .std-licence { left: 178px; top: 186px; font-size: 8px; }
  .lic-no { left: 37px; top: 183px; font-size: 11px; font-weight: 500; }
  .crush-note { left: 81px; top: 210px; font-size: 11px; font-weight: 500; letter-spacing: 0.2px; }
  .mark-row {
    position: absolute; left: 55px; top: 232px;
    display: flex; gap: 11px; align-items: center;
  }
  .mark-row span { display: block; width: 19px; height: 19px; background: var(--ink-soft); }
  .mark-row .round { border-radius: 50%; }
  .mark-row .square { border-radius: 3px; }

  /* Centre panel */
  .net-qty { left: 559px; top: 24px; font-size: 9px; font-weight: 500; }
  .mountain-art {
    position: absolute; left: 348px; top: 48px; width: 245px; height: 93px;
    border-radius: 6px;
    background: linear-gradient(180deg, var(--art-hi) 0%, var(--art-lo) 100%);
  }
  .brand {
    position: absolute; left: 341px; top: 154px; width: 256px;
    display: flex; align-items: center; justify-content: center; gap: 8px;
  }
  .brand-name { font-size: 48px; font-weight: 600; letter-spacing: 1.5px; line-height: 1; }
  .brand-dot { width: 14px; height: 14px; border-radius: 50%; background: var(--ink); }
  .product-type {
    position: absolute; left: 341px; top: 215px; width: 256px; text-align: center;
    font-size: 14px; font-weight: 500; letter-spacing: 0.4px;
  }

  /* Right panel */
  .about { left: 675px; top: 23px; width: 212px; font-size: 9px; line-height: 12.4px; white-space: normal; }
  .nutrition-title { left: 675px; top: 80px; font-size: 11px; font-weight: 500; }
  .nutrition-title small { font-size: 8.5px; font-weight: 400; }
  .nutrition-table {
    position: absolute; left: 675px; top: 96px;
    display: grid; grid-template-columns: 66px 66px 90px;
    font-size: 8.4px; line-height: 1.45;
  }
  .cert-info { left: 675px; top: 136px; font-size: 8.6px; font-weight: 500; }
  .batch-info { left: 675px; top: 150px; font-size: 8.4px; line-height: 1.45; }
  .contact {
    position: absolute; left: 675px; top: 180px;
    display: grid; grid-template-columns: 93px auto;
    font-size: 8.6px; font-weight: 500; line-height: 1.3;
  }
  .best-before { left: 675px; top: 208px; font-size: 11px; font-weight: 500; }
  .storage { left: 675px; top: 231px; font-size: 8.1px; line-height: 1.45; }
</style>
</head>
<body>
  <section class="wrap-label">
    <div class="edge-tab edge-tab--top"></div>
    <div class="edge-tab edge-tab--bottom"></div>

    <div class="block maker">
      <p class="caption">Manufactured By:</p>
      <p class="name">Tarini Aqua Works Pvt Ltd</p>
      <p class="address">Plot 14, Riverside Estate, Nandpur, Rampur District - 110045</p>
    </div>

    <div class="block marketer">
      <p class="caption">Marketed By:</p>
      <p class="name">BlueCrest Traders</p>
      <p class="address">Second Floor, Lake View Colony, Ramghat, Nandpur,<br>Rampur District - 110045</p>
    </div>

    <div class="cert-badge cert-badge--food" role="img" aria-label="Food safety licence badge"></div>
    <p class="block std-code">IS 14543</p>
    <div class="cert-badge cert-badge--std" role="img" aria-label="Standards certification badge"></div>
    <p class="block lic-no">Lic. No. : 10098765400211</p>
    <p class="block std-licence">CM/L-4400218753</p>

    <p class="block crush-note">CRUSH THE BOTTLE AFTER USE</p>
    <div class="mark-row" role="img" aria-label="Disposal, recycling and compliance marks">
      <span class="square"></span>
      <span class="round"></span>
      <span class="round"></span>
      <span class="square"></span>
      <span class="round"></span>
      <span class="round"></span>
    </div>

    <p class="block net-qty">NET QTY 1L</p>
    <div class="mountain-art" role="img" aria-label="Illustration of snow-capped mountain peaks"></div>
    <div class="brand">
      <span class="brand-name">PURAVELN</span>
      <span class="brand-dot"></span>
    </div>
    <p class="product-type">PACKAGED DRINKING WATER</p>

    <p class="block about">Every Drop Of PuraVeln Water Goes Through A Multistage Purification Process That Includes Micron Filtration, Purification, UV, Ozonation And With Add Minerals (Calcium Chloride, Magnesium Sulphate &amp; Potassium Bicarbonate).</p>

    <p class="block nutrition-title">Nutritional Information <small>(Typical values per 100ml) :</small></p>
    <div class="nutrition-table">
      <span>Energy: 0 Kcal</span><span>Protein: 0 g</span><span>Carbohydrate: 0 g</span>
      <span>Calcium: 1.0 mg</span><span>Sugar: 0 g</span><span>Magnesium: 0.5mg</span>
      <span>Fat: 0 g</span><span>Potassium: 0.1 mg</span><span></span>
    </div>

    <p class="block cert-info">For Certification details, visit: www.stdcert.in</p>
    <p class="block batch-info">For Date of Manufacturing, Date of Packaging, Batch No.,<br>MRP(Incl. Of All Taxes), Usp &amp; Expiry: CHECK BOTTLE NECK/CAP</p>

    <div class="contact">
      <span>Customer Care:</span><span>+91-7300012345</span>
      <span>Email:</span><span>care@tariniaqua.in</span>
    </div>

    <p class="block best-before">BEST BEFORE 6 MONTHS FROM PACKAGING</p>
    <p class="block storage">Do not accept if Cap/Seal is broken. Store in Cool, Dry &amp; Hygienic place.<br>Keep the container away from direct sunlight.</p>
  </section>
</body>
</html>
```